A farm is looking for the unified design for the bags' and bottles' labels in their organic produ...

We are a farm that deals with the production and sale of the organic seeds and oils. From the seed programme, we offer the organic flax, sunflower, hemp and pumpkin seeds. In our program, the organic unrefined cold-pressed hemp, linseed and sunflower oil and cold-pressed pumpkin oil can be found.
Design wise, we want to unify our sales programme with a unique organic look of bottle labels containing organic oils and labels for paper bags containing seeds.
We intend to keep the appearance of the exiting logotype (refer to the logotype provided in the enclosed PDF file). Regarding the colours, our products should be separated by a colour scheme (hemp, flax, pumpkin seeds, sunflower, etc.). The label material should be the same for the bags and the bottles. If possible, we would like to utilize the ecological paper, together with the option of applying the labels using the organic glue (starch, etc.). Also, the possibility of the eventual later printing directly onto the packaging (paper bags and bottles) must be considered and envisioned.
Additionally, there should be space on the label for the written title of the product (for example, »BIO pumpkin seeds«) and some space for short indications, markings and data in the corners of the label. You can also include an image that will indicate the contents of the bag/bottle.
We will appreciate all your contributions.

IN DOMESTIC LANGUAGE:
Smo kmetija, ki se ukvarja s pridelavo in prodajo ekoloških semen in olj. Iz programa semen nudimo BIO lanena, sončnična, konopljina in bučna semena. V našem programu so BIO nerafinirano hladno stiskano konopljino, laneno ter sončnično olje in hladno stiskano bučno olje.
Želimo oblikovno poenotiti naš prodajni program z enotnim EKO videzom etiket za steklenice z BIO olji in etiket za papirnate vrečke z semeni.
Ohraniti nameravamo videz obstoječega logotipa (glej logotip v priloženi PDF datoteki). Barvno je treba ločiti proizvode po barvni shemi (konoplja, lan, bučno seme, sončnica …). Material etiket naj bo enak za vrečke in steklenice. Po možnosti naj gre za ekološki papir, pa tudi možnost nanosa etiket z ekološkim lepilom (škrob …). Predvideti je treba tudi možen kasnejši tisk neposredno na embalažo (papirnate vrečke ter steklenice).
Prav tako naj bo na etiketi prostor za napis naslova izdelka (na primer »BIO bučno seme«) in po robovih nekaj prostora za krajše navedbe, označbe ter podatke, vključena pa je lahko tudi slika, ki nakazuje na vsebino vrečke/steklenice.
Najlepša hvala že vnaprej za vaše prispevke.

```html
<!DOCTYPE html>
<html lang="en">
<head>
<meta charset="utf-8">
<title>BIO Sunflower Seeds – Label</title>
<link href="https://fonts.googleapis.com/css2?family=Titillium+Web:wght@300;700;900&family=Roboto+Condensed:wght@300;400;700&family=Archivo+Black&family=Lato:wght@400;700&display=swap" rel="stylesheet">
<style>
  :root{
    --stage:#2c2c2c;
    --sun:#fcc43c;
    --band:#2d2d2d;
    --ring:#f6a623;
    --seed-dark:#111;
    --seed-mid:#2a2a2a;
    --paper:#ffffff;
    --ink:#111111;
    --soft:#dcdcdc;
    --badge:#f4efe4;
  }
  *{box-sizing:border-box;margin:0;padding:0}
  html,body{width:1200px;height:835px;overflow:hidden;background:var(--stage)}
  .canvas{position:relative;width:1200px;height:835px}
  .label{position:absolute;left:84px;top:94px;width:1032px;height:646px;background:var(--sun)}
  .front-band{position:absolute;left:154px;top:0;width:204px;height:646px;background:var(--band)}
  .logo-slot{position:absolute;left:154px;top:50px;width:204px;text-align:center;color:var(--soft);
    font:300 21px/29px "Titillium Web",sans-serif;letter-spacing:.5px}
  .seal{position:absolute;left:60px;top:124px;width:392px;height:392px;border-radius:50%;
    border:4px solid var(--ring);background:radial-gradient(circle at 40% 35%,var(--seed-mid),var(--seed-dark) 75%)}
  .product-title{position:absolute;left:60px;width:392px;text-align:center;color:#fff;font-family:"Titillium Web",sans-serif}
  .product-title.bio{top:184px;font-weight:900;font-size:138px;line-height:130px;letter-spacing:-2px}
  .product-title.kind{top:313px;font-weight:700;font-size:40px;line-height:46px;letter-spacing:-.3px}
  .claims{position:absolute;left:174px;top:374px;width:164px;color:#eee;text-align:center;
    font:300 21px/28px "Titillium Web",sans-serif}
  .claims li{list-style:none;border-bottom:2px solid #ddd}
  .claims li:last-child{border-bottom:0}
  .cert-badge{position:absolute;left:212px;top:479px;width:94px;height:94px;border-radius:50%;background:var(--badge)}
  .net-weight{position:absolute;left:154px;top:601px;width:204px;text-align:center;color:#fff;
    font:400 12px "Lato",sans-serif;letter-spacing:-.3px}

  .facts-panel{position:absolute;left:558px;top:40px;width:431px;height:431px;background:var(--paper);
    padding:20px 26px 0 26px;color:var(--ink);font-family:"Roboto Condensed",sans-serif}
  .caution{font:300 14.6px/16px "Roboto Condensed",sans-serif;letter-spacing:-.2px}
  .caution b{font-weight:700}
  .facts{margin-top:6px;border:2px solid var(--ink);padding:0 3px 7px 3px}
  .facts h2{font:400 37px/40px "Archivo Black",sans-serif;display:flex;justify-content:space-between;letter-spacing:-.3px}
  .row{display:flex;font-weight:300;font-size:14px;line-height:16px}
  .row .dots{flex:1;border-bottom:2px dotted #333;margin:0 2px 4px}
  .bar{background:var(--ink);height:28px;margin-top:4px}
  .bar.mid{height:26px;margin-top:6px}
  .bar.thin{height:8px;margin-top:3px}
  .head{display:flex;justify-content:space-between;font:700 15px/18px "Roboto Condensed",sans-serif;margin-top:3px}
  .split{display:flex;justify-content:space-between;font-weight:300;font-size:14px;line-height:16px;margin-top:4px}
  .r-first{margin-top:4px}
  .r-blend{margin-top:3px}
  .r-dv{margin-top:2px}
  .note{font-weight:300;font-size:14px;line-height:16px;padding-left:6px}
  .other{font-weight:300;font-size:14px;line-height:16px;margin-top:3px}

  .copy{position:absolute;left:564px;top:490px;width:418px;font:700 12px/14.5px "Lato",sans-serif;color:var(--ink)}
  .company{position:absolute;left:564px;top:553px;color:var(--ink);font-family:"Lato",sans-serif}
  .company .tag{font-weight:700;font-size:12px}
  .company .name{font-weight:700;font-size:18px;line-height:22px;margin-top:3px}
  .company .mail{font-weight:700;font-size:12px}
  .barcode-slot{position:absolute;left:850px;top:550px;width:139px;height:81px;background:var(--ink);
    color:#fff;display:flex;align-items:center;justify-content:center;font:700 12px "Lato",sans-serif}
</style>
</head>
<body>
<div class="canvas">
  <section class="label">
    <div class="front-band"></div>
    <div class="logo-slot">YOUR LOGO<br>HERE</div>
    <div class="seal" role="img" aria-label="Close-up photograph of black sunflower seeds"></div>
    <div class="product-title bio">BIO</div>
    <div class="product-title kind">SUNFLOWER SEEDS</div>
    <ul class="claims">
      <li>• 100 % PURE</li>
      <li>• UNREFIEND</li>
      <li>• COLD-PRESSED</li>
    </ul>
    <div class="cert-badge" role="img" aria-label="Organic certification badge"></div>
    <div class="net-weight">NET WT. 7 OZ. (50 ML)</div>

    <div class="facts-panel">
      <p class="caution"><b>Caution:</b> This product is processed in a facility that manufactures other products containing soy, milk, egg, wheat, peanut, tree nuts, fish, and shellfish.</p>
      <div class="facts">
        <h2><span>Supplement</span><span>Facts</span></h2>
        <div class="split"><span>Serving Size: 1 Tablet</span><span>Servings per Container: 90</span></div>
        <div class="bar"></div>
        <div class="head"><span>Amount per Serving</span><span>%DV</span></div>
        <div class="bar thin"></div>
        <div class="row r-first"><span>Calories</span><span class="dots"></span><span style="width:124px">2</span></div>
        <div class="row"><span>Cholesterol</span><span class="dots"></span><span>5 mg</span><span class="dots" style="flex:0 0 80px"></span><span>2%</span></div>
        <div class="row"><span>Vitamin C</span><span class="dots"></span><span>5 mg</span><span class="dots" style="flex:0 0 74px"></span><span>10%</span></div>
        <div class="bar mid"></div>
        <div class="row r-blend"><span>Proprietary Blend</span><span class="dots" style="flex:0 0 150px"></span><span>370 mg</span></div>
        <p class="note">Calcium lactate, bovine thymus Thymerol™ extract†, and magnesium citrate.</p>
        <div class="bar"></div>
        <div class="row r-dv"><span>†Daily Value (DV) not established.</span></div>
      </div>
      <p class="other">Other Ingredients: Cellulose, ascorbic acid, and calcium stearate.</p>
    </div>

    <p class="copy">Lorem ipsum dolor sit amet, consectetuer adipiscing elit, sed diam nonummy nibh euismod tincidunt ut laoreet dolore magna aliquam erat volutpat. Ut wisi enim ad minim veniam, quis nostrud exerci tation ullamcorper suscipit lobortis nisl ut aliquip ex ea commodo</p>
    <div class="company">
      <div class="tag">Compnay infohere:</div>
      <div class="name">compnay name here</div>
      <div class="mail">hello@sunfieldfarm.example</div>
    </div>
    <div class="barcode-slot">barcode</div>
  </section>
</div>
</body>
</html>
```